Book Cover design Paws & Petals Book Cover

Please see attached brief Book title BRAVE BESIDE TAILS AND TIDES
THE QUIET GIFT OF CANINES IN LIVING AND HEALING (INCLUSIVE OF THERAPY, EDUCATION, PARENTING, CARE) I have attached a word document describing the brief. Essentially book cover should include a dog and a person, perhaps an older person and a child, and a dog, emotionally charged faces, no cartoons, happy with designer to play with concept and ideas, please avoid AI looking images.

Target Market(s)

Parents, therapists, teachers, people who work with patients/vulnerable people

Industry/Entity Type

Therapeutic care, education, non fiction

Font styles to use
Sans Serif

Requirements
Must have
• Warmth, emotion. I have included the Author photo and paragraph for the back, and also the spec in the details.

```html
<!DOCTYPE html>
<html lang="en">
<head>
<meta charset="utf-8">
<title>Brave Beside Tails and Tides – Book Cover Wrap</title>
<link rel="stylesheet" href="https://fonts.googleapis.com/css2?family=Bebas+Neue&family=Arimo:ital,wght@1,700&display=swap">
<style>
  :root {
    --orange: #f1772b;
    --spine-orange: #f07c33;
    --ink: #1c1b1b;
    --white: #ffffff;
    --sky-top: #7f95a8;
    --sky-mid: #c7c9c2;
    --dusk-dark: #2c2f33;
    --gold: #e79a3c;
    --sun: #fff1c8;
    --field: #3a2a14;
  }
  * { margin: 0; padding: 0; box-sizing: border-box; }
  html, body { width: 1200px; height: 857px; overflow: hidden; background: #ffffff; }
  .cover {
    position: relative;
    width: 1200px;
    height: 857px;
    overflow: hidden;
    font-family: "Arimo", Arial, sans-serif;
  }
  .backdrop {
    position: absolute; inset: 0;
    background:
      radial-gradient(ellipse 260px 140px at 690px 540px, var(--sun) 0%, rgba(255,220,150,0.75) 30%, rgba(231,154,60,0) 100%),
      radial-gradient(ellipse 420px 220px at 700px 560px, rgba(240,170,80,0.7) 0%, rgba(240,170,80,0) 100%),
      linear-gradient(90deg, rgba(20,24,30,0.55) 0%, rgba(20,24,30,0.15) 45%, rgba(0,0,0,0) 60%),
      linear-gradient(180deg, var(--sky-top) 0%, #a9b4b9 28%, var(--sky-mid) 45%, var(--gold) 62%, #8a5a24 75%, var(--field) 100%);
  }
  .front-scene {
    position: absolute; left: 740px; top: 440px; width: 460px; height: 280px;
    background: radial-gradient(ellipse at 55% 60%, rgba(90,60,35,0.45) 0%, rgba(90,60,35,0) 70%);
  }

  /* Back cover */
  .blurb {
    position: absolute; left: 102px; top: 108px; width: 380px;
    color: var(--white); font-weight: 700; font-style: italic;
    font-size: 15.4px; line-height: 20px;
    text-shadow: 0 1px 2px rgba(0,0,0,0.45);
  }
  .back-rule {
    position: absolute; left: 142px; top: 358px; width: 292px; height: 5px;
    background: var(--orange);
  }
  .author-photo {
    position: absolute; left: 220px; top: 377px; width: 140px; height: 176px;
    border: 3px solid var(--white);
    background: radial-gradient(ellipse at 50% 40%, #5a4f5e 0%, #2a2430 70%, #1d1a22 100%);
  }
  .bio {
    position: absolute; left: 108px; top: 567px; width: 370px;
    color: var(--white); font-weight: 700; font-style: italic;
    font-size: 12.2px; line-height: 15.6px;
    text-shadow: 0 1px 2px rgba(0,0,0,0.4);
  }
  .code-box {
    position: absolute; left: 359px; top: 712px; width: 185px; height: 110px;
    background: var(--white);
  }

  /* Spine */
  .spine {
    position: absolute; left: 568px; top: 0; width: 65px; height: 857px;
    background: var(--spine-orange);
  }
  .spine-title, .spine-author {
    position: absolute; left: 50%;
    font-family: "Bebas Neue", Impact, sans-serif;
    white-space: nowrap;
    transform-origin: 0 0;
    transform: rotate(90deg);
  }
  .spine-title {
    top: 136px; margin-left: 12px;
    font-size: 25px; letter-spacing: 0.2px; color: var(--ink);
  }
  .spine-author {
    top: 454px; margin-left: 13px;
    font-size: 27px; color: var(--white);
  }
  .spine-author small { font-size: 14px; }

  /* Front cover */
  .title {
    position: absolute; left: 730px; top: 84px; width: 380px;
    font-family: "Bebas Neue", Impact, sans-serif; font-weight: 400;
    color: var(--ink);
  }
  .title span { display: block; }
  .title-lead { color: var(--orange); font-size: 158px; line-height: 136px; letter-spacing: 1px; }
  .title-line { font-size: 88px; line-height: 76px; }
  .subtitle {
    position: absolute; left: 700px; top: 372px; width: 420px; text-align: center;
    font-family: "Bebas Neue", Impact, sans-serif;
    color: var(--orange); font-size: 31px; line-height: 28px; letter-spacing: 0.3px;
  }
  .front-author {
    position: absolute; left: 725px; top: 734px;
    font-family: "Bebas Neue", Impact, sans-serif;
    color: var(--white); font-size: 54px; line-height: 1; white-space: nowrap;
  }
  .front-author small { font-size: 26px; margin-right: 2px; }
</style>
</head>
<body>
<main class="cover">
  <div class="backdrop" role="img" aria-label="Photograph of an open grassy field at sunset, hazy blue sky fading into golden light over distant hills"></div>
  <div class="front-scene" role="img" aria-label="Photograph of a smiling older man in a flat cap sitting on the grass with a young child in an orange hoodie and a tricolour dog wearing a purple neck wrap"></div>

  <section class="back">
    <p class="blurb">Brave Beside Tails and Tides is a practical and reflective book about the role of dogs in everyday emotional life. It draws on real experience from therapeutic work, education, parenting, and care, showing how dogs offer consistency, comfort and connection during difficult times, and how they in general provide consistent support in growth and learning. It’s written for professionals, parents and carers who live or work alongside dogs in emotionally complex situations and want something honest, useful and grounded in real practice.</p>
    <div class="back-rule"></div>
    <div class="author-photo" role="img" aria-label="Author portrait photograph against a dark studio backdrop"></div>
    <p class="bio">Dr Eleanor Hayes is the CEO of Marrowfield. She leads national work in therapeutic education, trauma-informed care, and animal-assisted interventions. Eleanor has over 20 years’ experience across social work, mental health and leadership, and is a parent of three. Her work combines lived experience with professional insight, with a focus on what helps in real life  not just in theory.</p>
    <div class="code-box"></div>
  </section>

  <section class="spine">
    <div class="spine-title">BRAVE BESIDE TAILS AND TIDES</div>
    <div class="spine-author"><small>DR</small> ELEANOR HAYES</div>
  </section>

  <section class="front">
    <h1 class="title">
      <span class="title-lead">BRAVE</span>
      <span class="title-line">BESIDE TAILS</span>
      <span class="title-line">AND TIDES</span>
    </h1>
    <p class="subtitle">THE QUIET GIFT OF CANINES<br>IN LIVING AND HEALING</p>
    <p class="front-author"><small>DR</small>ELEANOR HAYES</p>
  </section>
</main>
</body>
</html>
```